Calloway Winery Wine Label Re-design

Calloway Winery is located in the Finger Lakes region of New York. The Calloway Family planted the first vineyards in 1979 and opened in 1986. We produce award winning premium, hand crafted estate grown wines. We are in the process of a wine label re-design across our entire line. We would like to have the new label 'pop' but still convey elegance and ultra-premium quality. We are open to all color and styles or a minimalist design.
The attached files contain our new logo and samples of our current label (marked current) with dimensions. Our labeler is limited to label shapes but does not necessarily to have to be die-cut(the top arch) like our current label.

Target Market(s)

Upper income quality wine drinkers

Colors

Designer to choose colors to be used in the design.

Requirements
Should not have
• Should not be a tranparent label

```html
<!DOCTYPE html>
<html lang="en">
<head>
<meta charset="utf-8">
<title>Calloway Winery – Label Concepts</title>
<link rel="stylesheet" href="https://fonts.googleapis.com/css2?family=Cormorant+Garamond:wght@400;500&family=Montserrat:wght@400&family=Pinyon+Script&display=swap">
<style>
  :root {
    --paper: #ffffff;
    --ink-black: #0b0b0b;
    --gold: #b88a2c;
    --gold-light: #e9cf7d;
    --gold-deep: #8c6418;
    --sage: #8a8e85;
    --grey-text: #8d8d8d;
    --varietal-grey: #7a7a7a;
    --label-edge: #e4e4e4;
  }
  * { box-sizing: border-box; margin: 0; padding: 0; }
  html, body { width: 1200px; height: 848px; overflow: hidden; background: var(--paper); }
  .sheet { position: relative; width: 1200px; height: 848px; font-family: "Cormorant Garamond", Georgia, serif; }

  .label { position: absolute; left: 152px; width: 232px; height: 356px; }
  .label--white { top: 45px; background: var(--paper); border: 1px solid var(--label-edge); }
  .label--black { top: 411px; background: var(--ink-black); }

  .label > * { position: absolute; left: 0; width: 100%; text-align: center; line-height: 1; }

  .label__tagline {
    font-family: "Montserrat", Arial, sans-serif; font-size: 5.5px; letter-spacing: 1.6px; color: var(--grey-text);
  }
  .label--black .label__tagline { color: #c4c4c4; }

  .brand { display: flex; flex-direction: column; align-items: center; color: var(--gold); font-weight: 500; }
  .brand__dot { width: 30px; height: 30px; border-radius: 50%; background: var(--gold); margin-bottom: 10px; }
  .brand__name { font-size: 18px; letter-spacing: 3.5px; line-height: 1; }
  .brand__sub { font-size: 9px; letter-spacing: 4.5px; margin-top: 2px; line-height: 1; }

  .vintage { font-size: 10px; letter-spacing: 4px; font-variant-numeric: lining-nums; }
  .varietal { font-size: 17px; letter-spacing: 3px; line-height: 1.2; }
  .label--white .vintage, .label--white .varietal { color: var(--varietal-grey); }
  .label--black .vintage, .label--black .varietal { color: #ececec; }

  .script-motto { font-family: "Pinyon Script", cursive; color: var(--gold); font-size: 18px; white-space: nowrap; }

  .label__band {
    top: auto !important; bottom: 0; height: 17px;
    background: linear-gradient(90deg, var(--gold-deep), var(--gold-light) 45%, var(--gold) 70%, var(--gold-light));
    font-family: "Montserrat", Arial, sans-serif; font-size: 5.5px; letter-spacing: 2.6px;
    color: #5a3f0c; display: flex; align-items: center; justify-content: center;
  }

  .lockup { position: absolute; left: 564px; top: 0; width: 400px; height: 300px; }
  .lockup > * { position: absolute; left: 0; width: 100%; text-align: center; line-height: 1; }
  .lockup .brand { top: 78px; color: var(--sage); }
  .lockup .brand__dot { width: 40px; height: 40px; background: var(--sage); margin-bottom: 14px; }
  .lockup .brand__name { font-size: 27px; letter-spacing: 4px; }
  .lockup .brand__sub { font-size: 13px; letter-spacing: 7px; margin-top: 2px; }
  .lockup .script-motto { top: 190px; font-size: 46px; }
  .lockup__est { top: 264px; font-family: "Montserrat", Arial, sans-serif; font-size: 8px; letter-spacing: 3px; color: var(--grey-text); }
</style>
</head>
<body>
<main class="sheet">

  <section class="label label--white">
    <p class="label__tagline" style="top:12px">ESTATE GROWN AND BOTTLED</p>
    <div class="brand" style="top:52px">
      <span class="brand__dot"></span>
      <span class="brand__name">CALLOWAY</span>
      <span class="brand__sub">WINERY</span>
    </div>
    <p class="vintage" style="top:208px">2013</p>
    <p class="varietal" style="top:227px">CHARDONNAY</p>
    <p class="script-motto" style="top:277px">Our Passion is Wine</p>
    <p class="label__band">WINERY AND VINEYARDS</p>
  </section>

  <section class="label label--black">
    <p class="label__tagline" style="top:12px">ESTATE GROWN AND BOTTLED</p>
    <div class="brand" style="top:54px">
      <span class="brand__dot"></span>
      <span class="brand__name">CALLOWAY</span>
      <span class="brand__sub">WINERY</span>
    </div>
    <p class="vintage" style="top:209px">2013</p>
    <p class="varietal" style="top:228px">CABERNET<br>SAUVIGNON</p>
    <p class="script-motto" style="top:285px">Our Passion is Wine</p>
    <p class="label__band">WINERY AND VINEYARDS</p>
  </section>

  <section class="lockup">
    <div class="brand">
      <span class="brand__dot"></span>
      <span class="brand__name">CALLOWAY</span>
      <span class="brand__sub">WINERY</span>
    </div>
    <p class="script-motto">Our Passion is Wine</p>
    <p class="lockup__est">EST-1979</p>
  </section>

</main>
</body>
</html>
```